B2B telecom company need web design

We need a web design for our corporate web site. The company exists since almost 10 years.
This is a DESIGN contest, you're expected to provide design only, NOT the whole website. The winner will have to provide the HTML template (with Lorem Ipsum content) and the CSS files of his design.
Our initial product is SMS peering in P2P (you send a SMS to a friend in a foreign country, great chance that your operator route your SMS to us that we route to the recipient). We're launching a bulk SMS service (marketing and application to SMS).
Target is mostly corporate, usually big corporate (operators, contents providers...) where use of SMS is part of the main business.
The web site is composed of 1 landing page and 7 content pages (plan is given for your information, all content page are using the same template and the same design, you do NOT need to make one design per page) :
* About US
Company Profile
They trust us
The Volnor Team
Partners
Contact us
* Solution
P2P SMS
A2P SMS
You only need to submit the landing page and a template page for the content (with h1, h2, h3 and h4).
Design must be based on our new logo (see attached file).
Our current web site http://www.volnor-example.com
The winner of the contest will have to provide state of the art HTML template and CSS files of his design. Photo used shall be downloaded from Pixelbrook (provide the ID of the picture that we purchase file).
Target Market(s)
Telecom operator. SMS Peering hubs. Bulk SMS.
Industry/Entity Type
It Company
Number of Pages Required
2 page

```html
<!DOCTYPE html>
<html lang="en">
<head>
<meta charset="utf-8">
<title>Volnor Mobile</title>
<link rel="stylesheet" href="https://fonts.googleapis.com/css2?family=Roboto:wght@300;400;500;700&family=Roboto+Condensed:wght@400;700&display=swap">
<style>
:root{
  --green:#7cc12b;
  --ink:#222;
  --dark-1:#16191c;
  --dark-2:#3a3f44;
  --footer:#2b2b2b;
  --footer-text:#d8d8d8;
  --icon-grey:#9a9a9a;
  --white:#fff;
}
*{box-sizing:border-box;margin:0;padding:0}
html,body{width:748px;height:1200px;overflow:hidden}
body{position:relative;font-family:"Roboto",Arial,sans-serif;background:var(--white);color:var(--ink)}
.abs{position:absolute}

/* intro band with blurred office backdrop */
.intro{left:0;top:0;width:748px;height:623px;
  background:radial-gradient(ellipse 70% 55% at 72% 42%,#53585e 0%,#33383d 40%,#22262a 70%,var(--dark-1) 100%)}

.logo{left:119px;top:11px;width:114px;height:58px;background:var(--white);
  display:flex;align-items:center;justify-content:center;
  font:500 12.5px "Roboto",sans-serif;color:#3a3a3a;letter-spacing:.4px}

.nav-link{top:31px;font:400 9px/19px "Roboto",sans-serif;color:var(--white);text-decoration:none;text-transform:uppercase}
.nav-link.is-active{background:var(--green);padding:0 12px;border-radius:4px}

.hero{left:119px;top:80px;width:510px;height:224px;
  background:radial-gradient(ellipse 32% 40% at 85% 50%,#f4fbff 0%,#9fd3f2 25%,rgba(43,128,190,0) 70%),
             linear-gradient(100deg,#2a2c30 0%,#6f6460 18%,#2c5d86 38%,#1f70ad 60%,#2a88c6 80%,#1b4e7a 100%)}
.hero-title{left:132px;top:108px;font:700 24px/25px "Roboto Condensed",sans-serif;color:var(--white);text-transform:uppercase;letter-spacing:.2px}

.welcome-title{left:0;top:330px;width:748px;text-align:center;font:400 19px "Roboto",sans-serif;color:var(--white);text-transform:uppercase}
.welcome-text{left:128px;top:362px;width:492px;text-align:center;font:400 7.3px/10.4px "Roboto",sans-serif;color:#e8e8e8}

.feature-circle{width:65px;height:65px;border-radius:50%;background:var(--white);border:3px solid var(--green);display:flex;align-items:center;justify-content:center}
.feature-label{font:400 12px "Roboto",sans-serif;color:var(--white);white-space:nowrap}
.feature-art{left:300px;top:474px;width:146px;height:102px;
  background:radial-gradient(ellipse 50% 50% at 50% 50%,#f3c02d 0%,#d9a51e 25%,#7d94aa 48%,rgba(60,70,80,0) 72%)}

/* services */
.section-title{left:0;top:648px;width:748px;text-align:center;font:400 18px "Roboto",sans-serif;color:var(--ink);text-transform:uppercase}
.service-name{width:154px;text-align:center;top:687px;font:400 11px "Roboto Condensed",sans-serif;color:var(--green);text-transform:uppercase}
.service-photo{top:712px;width:154px;height:99px}
.photo-team{left:119px;background:linear-gradient(90deg,#2d2420 0%,#c9a48c 22%,#f1ebe6 45%,#d8c1ae 65%,#4a4a4e 85%,#e8e8e8 100%)}
.photo-network{left:297px;border:1px solid var(--green);background:radial-gradient(ellipse 45% 50% at 50% 40%,#2f6fb4 0%,#7fb0dc 35%,#f0c53a 60%,#f7f7f7 85%)}
.photo-keyboard{left:476px;background:linear-gradient(135deg,#eef0f2 0%,#c5cacf 40%,#2f86d6 62%,#e4c6ad 80%,#f1f1f1 100%)}

.map{left:0;top:845px;width:748px;height:198px;
  background:linear-gradient(100deg,#a9d0ec 0%,#b9d9ea 14%,#d9e4b8 24%,#e7e2c4 45%,#c6dba8 60%,#e3e0bf 75%,#d4e3ac 100%)}

/* footer */
.footer{left:0;top:1043px;width:748px;height:157px;background:var(--footer)}
.foot-head{top:1065px;font:400 12px "Roboto Condensed",sans-serif;color:var(--white);text-transform:uppercase}
.foot-list{top:1087px;font:400 7.8px/10.5px "Roboto",sans-serif;color:var(--footer-text);list-style:none}
.social{left:573px;top:1089px;display:flex;gap:5px}
.social span{width:9px;height:9px;border-radius:50%;background:var(--icon-grey)}
.copyright{left:0;top:1165px;width:748px;text-align:center;font:400 7.5px "Roboto",sans-serif;color:var(--footer-text)}
</style>
</head>
<body>

<section class="abs intro" aria-label="Welcome"></section>

<div class="abs logo">VOLNOR mobile</div>
<nav>
  <a href="#" class="abs nav-link is-active" style="left:345px">Home</a>
  <a href="#" class="abs nav-link" style="left:403px">About us</a>
  <a href="#" class="abs nav-link" style="left:463px">Our services</a>
  <a href="#" class="abs nav-link" style="left:537px">News</a>
  <a href="#" class="abs nav-link" style="left:581px">Contact us</a>
</nav>

<div class="abs hero" role="img" aria-label="Hand holding a phone sending text messages to a glowing laptop"></div>
<h1 class="abs hero-title">Get your SMS delivered<br>instantly</h1>

<h2 class="abs welcome-title">Welcome to Volnor Mobile</h2>
<p class="abs welcome-text">Lorem ipsum dolor sit amet, consectetur adipiscing elit. Praesent at tincidunt dolor, nec pulvinar elit. Vivamus imperdiet ipsum lacus, eu suscipit lacus maximus sed. Donec a posuere magna. Fusce finibus, elit nec semper convallis, odio magna feugiat nibh, eget feugiat elit nunc eu erat. Vestibulum ante ipsum primis in faucibus orci luctus et ultrices posuere cubilia Curae; Aliquam ac ipsum in mi luctus bibendum ac vitae nibh. Cras malesuada consequat dui, efficitur ultrices lectus aliquam ut. Nulla congue sollicitudin suscipit. Phasellus luctus fringilla diam convallis elementum. Curabitur quis lobortis est. Proin venenatis luctus efficitur.</p>

<!-- features -->
<span class="abs feature-label" style="left:131px;top:471px">Mobile Advantage</span>
<div class="abs feature-circle" style="left:231px;top:449px">
  <svg width="30" height="30" viewBox="0 0 30 30" fill="none" stroke="var(--green)" stroke-width="2"><rect x="5" y="4" width="20" height="16" rx="2"/><path d="M10 20l-2 6 7-6"/><path d="M10 10h10M10 14h7"/></svg>
</div>
<span class="abs feature-label" style="left:131px;top:551px">Mobile Solutions</span>
<div class="abs feature-circle" style="left:231px;top:528px">
  <svg width="30" height="30" viewBox="0 0 30 30" fill="none" stroke="var(--green)" stroke-width="2"><rect x="9" y="3" width="12" height="24" rx="2"/><path d="M13 24h4"/><path d="M17 10l-3 4h3l-3 4"/></svg>
</div>
<div class="abs feature-art" role="img" aria-label="Smartphone with yellow envelopes flying out of its screen"></div>
<div class="abs feature-circle" style="left:453px;top:449px">
  <svg width="30" height="30" viewBox="0 0 30 30" fill="none" stroke="var(--green)" stroke-width="2"><rect x="8" y="3" width="14" height="24" rx="2"/><path d="M11 17l2-6 2 4 2-4 2 6"/></svg>
</div>
<span class="abs feature-label" style="left:523px;top:471px">Mobile Interoperability</span>
<div class="abs feature-circle" style="left:453px;top:528px">
  <svg width="32" height="32" viewBox="0 0 32 32" fill="none" stroke="var(--green)" stroke-width="2"><circle cx="16" cy="16" r="12"/><path d="M6 12c6 2 8-4 12-2s2 6 8 4M10 26c2-4 6-4 8-8"/></svg>
</div>
<span class="abs feature-label" style="left:523px;top:551px">Techonology</span>

<!-- services -->
<h2 class="abs section-title">Our Services</h2>
<h3 class="abs service-name" style="left:119px">Operator Services</h3>
<h3 class="abs service-name" style="left:297px">Brand &amp; Content Services</h3>
<h3 class="abs service-name" style="left:476px">Enterprise Services</h3>
<div class="abs service-photo photo-team" role="img" aria-label="Customer support team wearing headsets"></div>
<div class="abs service-photo photo-network" role="img" aria-label="Globe surrounded by phones exchanging messages"></div>
<div class="abs service-photo photo-keyboard" role="img" aria-label="Finger pressing a blue key on a keyboard"></div>

<div class="abs map" role="img" aria-label="Map of Europe and western Asia showing office locations"></div>

<!-- footer -->
<footer class="abs footer"></footer>
<h4 class="abs foot-head" style="left:118px">Important Link</h4>
<ul class="abs foot-list" style="left:118px">
  <li>Privacy Policy</li><li>Legal Use</li><li>Anti-Spam Policy</li><li>Site Map</li>
</ul>

<h4 class="abs foot-head" style="left:245px">Contact us</h4>
<svg class="abs" style="left:245px;top:1088px" width="8" height="11" viewBox="0 0 8 11"><path d="M4 0a4 4 0 0 0-4 4c0 3 4 7 4 7s4-4 4-7a4 4 0 0 0-4-4z" fill="#bbb"/><circle cx="4" cy="4" r="1.5" fill="var(--footer)"/></svg>
<ul class="abs foot-list" style="left:258px">
  <li>Global Sales Offices</li><li>Headquarters (Geneva - Switzerland)</li><li>Rue des Lilas 14</li><li>CH-1200 Geneva</li>
</ul>

<svg class="abs" style="left:415px;top:1089px" width="11" height="8" viewBox="0 0 11 8"><rect width="11" height="8" fill="#bbb"/><path d="M0 0l5.5 4.5L11 0" stroke="var(--footer)" fill="none"/></svg>
<ul class="abs foot-list" style="left:431px">
  <li>info@volnor-mobile.com</li><li>emea@volnor-mobile.com</li><li>apac@volnor-mobile.com</li>
</ul>
<svg class="abs" style="left:416px;top:1119px" width="7" height="11" viewBox="0 0 7 11"><rect width="7" height="11" rx="1" fill="#bbb"/><rect x="1" y="1.5" width="5" height="7" fill="var(--footer)"/></svg>
<ul class="abs foot-list" style="left:431px;top:1120px"><li>+41 22 555 01 48</li></ul>

<h4 class="abs foot-head" style="left:572px">Follow us</h4>
<div class="abs social"><span></span><span></span></div>

<p class="abs copyright">© Copyright 2015, VOLNOR Mobile, All rights reserved</p>

</body>
</html>
```